Sleek and Morden Business Card

Business Card Design for Business Name "Lantern Pine Services (LPS)"
Offering Virtual Assistant (VA) services including Virtual Receptionist, Appointment and Diary Management. Taking and Answering calls for Sole Trader Businesses. Quotes, Invoices, Expense Reconciliation, Accounts Payable and Accounts Receivable.
Lantern Services offers clients the ease of a complete office without the physical need to having an office.
Target Market(s)
Target market are Sole Traders like Electricians, Plumbers, Painters etc.
Industry/Entity Type
Business
Colors
Designer to choose colors to be used in the design.
Look and feel
Each slider illustrates characteristics of the customer's brand and the style your logo design should communicate.

```html
<!DOCTYPE html>
<html lang="en">
<head>
<meta charset="utf-8">
<title>Lantern Pine Services – Business Card</title>
<link rel="stylesheet" href="https://fonts.googleapis.com/css2?family=Cormorant+Garamond:ital,wght@1,600&family=Cabin:ital,wght@0,400;0,500;1,700&family=Tinos&family=Parisienne&display=swap">
<style>
  :root {
    --brand-red: #d81f4a;
    --band-black: #1e1c1d;
    --paper: #ffffff;
    --ink: #222222;
    --list-ink: #3a3a3a;
    --frame: #8a8a8a;
    --logo-grey: #8c8c8c;
  }
  * { box-sizing: border-box; margin: 0; padding: 0; }
  html, body { width: 1200px; height: 800px; overflow: hidden; background: var(--paper); }
  .canvas { position: relative; width: 1200px; height: 800px; }

  .card {
    position: absolute; top: 15px; width: 440px; height: 772px;
    background: var(--paper); border: 1px solid var(--frame); overflow: hidden;
  }
  .card--front { left: 121px; }
  .card--back { left: 717px; }

  .card__title {
    position: absolute; left: 0; top: 0; width: 100%; height: 83px;
    background: var(--brand-red); color: var(--paper);
    font-family: "Cormorant Garamond", serif; font-style: italic; font-weight: 600;
    font-size: 40px; display: flex; align-items: center; justify-content: center;
    letter-spacing: 0.3px;
  }
  .card__stripe { position: absolute; left: 0; width: 100%; background: var(--band-black); }
  .card--front .card__stripe--top { top: 83px; height: 9px; }
  .card--back .card__stripe--top { top: 83px; height: 28px; }
  .card__stripe--bottom { top: 647px; height: 26px; }

  .card__footer {
    position: absolute; left: 0; top: 673px; width: 100%; height: 99px;
    background: var(--brand-red); color: var(--paper);
    font-family: "Tinos", serif; font-size: 35px; line-height: 1.2;
    display: flex; align-items: center; justify-content: center; text-align: center;
  }

  /* Front */
  .hero-art {
    position: absolute; left: 14px; top: 100px; width: 180px; height: 145px;
    background: radial-gradient(ellipse at 50% 45%, #e9d9c9 0%, #d9d0c8 45%, #f4f1ee 80%);
    border-radius: 8px;
  }
  .hero-question {
    position: absolute; right: 28px; top: 100px; width: 200px;
    font-family: "Tinos", serif; font-size: 32px; line-height: 1.28;
    color: var(--brand-red); text-align: center;
  }
  .help-bar {
    position: absolute; left: 0; top: 251px; width: 100%; height: 43px;
    background: var(--band-black); color: var(--paper);
    font-family: "Tinos", serif; font-size: 21px;
    display: flex; align-items: center; justify-content: center;
  }
  .help-bar strong { color: var(--brand-red); font-weight: 400; }

  .list-mark {
    position: absolute; left: 175px; top: 300px; width: 150px; height: 215px;
    background: radial-gradient(ellipse, rgba(0,0,0,0.07) 0%, rgba(0,0,0,0) 70%);
  }
  .service-list {
    position: absolute; left: 30px; top: 320px; width: 400px;
    list-style: none; font-family: "Cabin", sans-serif; font-size: 26px;
    color: var(--list-ink); line-height: 40px;
  }
  .service-list li { position: relative; padding-left: 35px; }
  .service-list li::before {
    content: ""; position: absolute; left: 3px; top: 17px;
    width: 7px; height: 7px; border-radius: 50%; background: var(--ink);
  }
  .service-list li.wrap { line-height: 27px; padding-top: 7px; }
  .service-list li.wrap::before { top: 17px; }
  .more {
    position: absolute; left: 0; top: 583px; width: 100%; text-align: center;
    font-family: "Cabin", sans-serif; font-style: italic; font-weight: 700;
    font-size: 31px; color: var(--ink);
  }

  /* Back */
  .brand-mark {
    position: absolute; left: 0; top: 150px; width: 100%;
    display: flex; align-items: center; justify-content: center; gap: 18px;
  }
  .brand-mark__dot { width: 34px; height: 34px; border-radius: 50%; background: var(--brand-red); }
  .brand-mark__name {
    font-family: "Cabin", sans-serif; font-weight: 500; font-size: 110px;
    color: var(--logo-grey); letter-spacing: 4px; line-height: 1;
  }
  .brand-tagline {
    position: absolute; left: 0; top: 325px; width: 100%; text-align: center;
    font-family: "Parisienne", cursive; font-size: 56px; color: var(--ink);
  }
  .holder-name {
    position: absolute; left: 0; top: 425px; width: 100%; text-align: center;
    font-family: "Cabin", sans-serif; font-size: 25px; color: var(--ink);
  }
  .contact {
    position: absolute; left: 0; top: 570px; width: 100%; text-align: center;
    font-family: "Cabin", sans-serif; color: var(--ink);
  }
  .contact__phone { font-size: 28px; letter-spacing: 1px; line-height: 1.2; }
  .contact__email { font-family: "Tinos", serif; font-size: 23px; line-height: 1.3; }
</style>
</head>
<body>
<main class="canvas">
  <section class="card card--front" aria-label="Front of card">
    <header class="card__title">Lantern Pine Services</header>
    <div class="card__stripe card__stripe--top"></div>
    <div class="hero-art" role="img" aria-label="Illustration of a busy assistant juggling office tasks"></div>
    <p class="hero-question">Tired of Juggling Too Many Tasks?</p>
    <p class="help-bar">Get the&nbsp;<strong>HELP</strong>&nbsp;you need, when you need it!</p>
    <div class="list-mark" role="img" aria-label="Faint decorative monogram"></div>
    <ul class="service-list">
      <li>Virtual Receptionist</li>
      <li>Expense Reconciliation</li>
      <li>Accounts Payable, Quotes</li>
      <li>Accounts Receivable</li>
      <li>Diary Management</li>
      <li class="wrap">Taking and Answering calls<br>for Sole Trader Businesses</li>
    </ul>
    <p class="more">And so much more...</p>
    <div class="card__stripe card__stripe--bottom"></div>
    <footer class="card__footer">Committed To Your<br>Company’s Success!</footer>
  </section>

  <section class="card card--back" aria-label="Back of card">
    <header class="card__title">Lantern Pine Services</header>
    <div class="card__stripe card__stripe--top"></div>
    <div class="brand-mark">
      <span class="brand-mark__dot"></span>
      <span class="brand-mark__name">LPS</span>
    </div>
    <p class="brand-tagline">Business Help</p>
    <p class="holder-name">Your Name</p>
    <address class="contact" style="font-style:normal">
      <p class="contact__phone">0400 555 218</p>
      <p class="contact__email">mara@lanternpine.com.au</p>
    </address>
    <div class="card__stripe card__stripe--bottom"></div>
    <footer class="card__footer">Committed To Your<br>Company’s Success!</footer>
  </section>
</main>
</body>
</html>
```